Singapore Restaurant Menu Design

We need a menu designed for our new Singapore inspire restaurant located here in New Plymouth New Zealand. More Information in attached documents.
Updates

Sick

Target Market(s)

New Zealanders

Colors

Designer to choose only greyscale colors for use in the design.

Requirements
Nice to have
• Images of Singapore food however we do not want this to distract from the overall menu design as we still want the menu to be super clean

```html
<!DOCTYPE html>
<html lang="en">
<head>
<meta charset="utf-8">
<title>Tanjong Table – Menu</title>
<link rel="stylesheet" href="https://fonts.googleapis.com/css2?family=Poppins:wght@400;500;600&display=swap">
<style>
  :root {
    --backdrop: #e2e2e2;
    --paper: #f3f3f1;
    --ink: #1c1c1c;
    --ink-soft: #555;
    --cover-dark: #0e0e0e;
    --cover-mid: #3a3a3a;
    --line-light: #f2f2f2;
    --accent-red: #d0201b;
  }
  * { box-sizing: border-box; margin: 0; padding: 0; }
  html, body { width: 1200px; height: 900px; overflow: hidden; }
  body {
    background: var(--backdrop);
    font-family: "Poppins", sans-serif;
    color: var(--ink);
    position: relative;
  }

  /* ---------- Cover ---------- */
  .cover {
    position: absolute; left: 24px; top: 200px;
    width: 340px; height: 500px;
    background: linear-gradient(160deg, var(--cover-mid) 0%, var(--cover-dark) 45%, var(--cover-dark) 100%);
    overflow: hidden;
  }
  .cover-lines { position: absolute; inset: 0; }
  .cover-ornament {
    position: absolute; left: 40px; top: 78px; width: 260px; height: 260px;
    background: radial-gradient(circle, #1a1a1a 45%, #6b6b6b 70%, #2a2a2a 100%);
  }
  .cover-brand {
    position: absolute; left: 40px; top: 78px; width: 260px; height: 260px;
    display: flex; flex-direction: column; align-items: center; justify-content: center;
    color: var(--line-light); text-align: center;
  }
  .brand-name {
    font-weight: 500; font-size: 27px; letter-spacing: 4px; text-transform: uppercase; line-height: 1.1;
  }
  .cover-tagline {
    position: absolute; left: 0; right: 0; bottom: 92px;
    text-align: center; color: var(--line-light);
    font-size: 9px; letter-spacing: 1px; text-transform: uppercase;
  }

  /* ---------- Inside spread ---------- */
  .spread {
    position: absolute; left: 392px; top: 170px;
    width: 784px; height: 560px;
    background: var(--paper);
    display: flex;
    box-shadow: 0 1px 3px rgba(0,0,0,.08);
  }
  .spread-frame { position: absolute; inset: 0; pointer-events: none; }
  .page { width: 392px; height: 100%; display: flex; padding: 30px 18px 30px 18px; gap: 14px; }
  .page + .page { border-left: 1px solid #d6d6d4; }
  .column { flex: 1; display: flex; flex-direction: column; }
  .column + .column { border-left: 1px dotted #9a9a9a; padding-left: 12px; }

  .section-title {
    text-align: center; font-weight: 600; font-size: 11px; letter-spacing: .5px;
    text-transform: uppercase; margin-bottom: 8px;
  }
  .section-title::after {
    content: ""; display: block; width: 34px; margin: 2px auto 0;
    border-top: 1px solid var(--ink); border-bottom: 1px solid var(--ink); height: 3px;
  }
  .dish { margin-bottom: 6.5px; }
  .dish-head { display: flex; justify-content: space-between; align-items: baseline; gap: 6px; }
  .dish-name { font-weight: 600; font-size: 6.6px; }
  .dish-price { font-weight: 500; font-size: 6.8px; white-space: nowrap; }
  .dish-desc { font-size: 5.8px; color: var(--ink-soft); line-height: 1.35; margin-top: 1px; padding-right: 18px; }
  .dish-note { color: var(--accent-red); font-weight: 500; }
  .dish-options { display: flex; gap: 10px; font-size: 5.8px; color: var(--ink-soft); margin-top: 1px; padding-left: 4px; }

  .photo {
    border: 1.5px solid var(--ink); outline: 1px solid var(--ink); outline-offset: 2px;
    margin: 3px 3px 12px;
  }
  .photo-crab { height: 130px; background: linear-gradient(135deg, #c7602e, #8a3a1c 60%, #5a6f6c); }
  .photo-pair { display: flex; height: 80px; }
  .photo-pair > div { flex: 1; }
  .photo-nasi { background: linear-gradient(160deg, #c44b2a, #e8e1d0 55%, #6f8a3f); }
  .photo-murtabak { background: linear-gradient(160deg, #2d2d2d, #d69a52 55%, #b13a28); }
  .photo-gado { height: 160px; margin-top: 8px; background: radial-gradient(circle, #e0b45a 0%, #7d9a4a 50%, #5a4a3a 100%); }
</style>
</head>
<body>

<section class="cover" aria-label="Menu cover">
  <svg class="cover-lines" width="340" height="500" viewBox="0 0 340 500" aria-hidden="true">
    <g stroke="#f2f2f2" fill="none" stroke-width="1.2">
      <line x1="28" y1="0" x2="28" y2="500"/><line x1="34" y1="0" x2="34" y2="500"/>
      <line x1="306" y1="0" x2="306" y2="500"/><line x1="312" y1="0" x2="312" y2="500"/>
      <line x1="28" y1="40" x2="312" y2="40"/>
      <line x1="28" y1="455" x2="312" y2="455"/>
    </g>
  </svg>
  <div class="cover-ornament" role="img" aria-label="Art deco geometric star frame ornament in white line work"></div>
  <div class="cover-brand">
    <span class="brand-name">Tanjong<br>Table</span>
  </div>
  <p class="cover-tagline">Singapore restaurant based in New Plymouth</p>
</section>

<main class="spread" aria-label="Menu inside spread">
  <svg class="spread-frame" width="784" height="560" viewBox="0 0 784 560" aria-hidden="true">
    <g stroke="#1c1c1c" fill="none" stroke-width="1">
      <line x1="18" y1="14" x2="370" y2="14"/><line x1="414" y1="14" x2="766" y2="14"/>
      <line x1="18" y1="546" x2="370" y2="546"/><line x1="414" y1="546" x2="766" y2="546"/>
      <polyline points="370,530 370,546 354,546"/><polyline points="414,30 414,14 430,14"/>
      <polyline points="766,530 766,546 750,546"/>
    </g>
  </svg>

  <div class="page">
    <div class="column">
      <h2 class="section-title">Starters</h2>
      <div class="dish"><div class="dish-head"><span class="dish-name">Vegetable Samosa V (3 pieces)</span><span class="dish-price">$3</span></div>
        <p class="dish-desc">Crispy pastries with fresh peas, potatoes &amp; spices coated in flour</p></div>
      <div class="dish"><div class="dish-head"><span class="dish-name">Tahu Goreng (Tofu with egg) V</span><span class="dish-price">$10</span></div>
        <p class="dish-desc">Flour coated tofu drenched in sweet satay sauce, crushed nuts &amp; sprouts.</p></div>
      <div class="dish"><div class="dish-head"><span class="dish-name">Epok Epok (Curry Puffs) (3 pieces)</span><span class="dish-price">$5</span></div>
        <p class="dish-desc">Malay style empanadas stuffed with choice of :</p>
        <div class="dish-options"><span>• Chicken curry<br>• Fork tender beef</span><span>• Curried potatoes &amp;<br>seasonal veggies</span></div></div>
      <div class="dish"><div class="dish-head"><span class="dish-name">Pakora V / Vegan</span><span class="dish-price">$5</span></div>
        <p class="dish-desc">Chickpea, red onion and potato fritters in a mildly spiced besan (chickpea flour) batter accompanied by a sweet tangy tamarind dip</p></div>
      <div class="dish"><div class="dish-head"><span class="dish-name">Chana Vada V / Vegan (3 pieces)</span><span class="dish-price">$5</span></div>
        <p class="dish-desc">Crunchy lentil fritters with onions, spices &amp; curry leaf</p></div>
      <div class="dish"><div class="dish-head"><span class="dish-name">Fried Wonton (8 pieces)</span><span class="dish-price">$10</span></div>
        <p class="dish-desc">Stuffed with choice of marinated spiced chicken / pork / pickled veggies with sweet soy dip</p></div>
      <div class="dish"><div class="dish-head"><span class="dish-name">Gado Gado Salad V / <span class="dish-note">*Vegan options available</span></span><span class="dish-price">$12</span></div>
        <p class="dish-desc">A delicate salad of thinly sliced chinese cabbage, cucumber, beansprout, potatoes, french beans tossed in peanut dressing with boiled egg &amp; marinated prawns.</p></div>
      <div class="dish"><div class="dish-head"><span class="dish-name">Satay (6 sticks)</span><span class="dish-price">$12</span></div>
        <p class="dish-desc">Grilled aromatic chicken / beef or tempeh (soy beans) on skewers accompanied by ketupat (rice cakes), cucumber, onions &amp; Singapore satay gravy</p></div>
      <div class="dish"><div class="dish-head"><span class="dish-name">BBQ Chicken Wings (5 pieces)</span><span class="dish-price">$15</span></div>
        <p class="dish-desc">Singapore style soy marinated BBQ chicken wings made to order with sweet chili dip</p></div>
      <div class="dish"><div class="dish-head"><span class="dish-name">Fried Carrot Cake</span><span class="dish-price">$10</span></div>
        <p class="dish-desc">Savoury steamed white radish cake stir-fry with prawns &amp; egg drizzled with sweet dark soy sauce</p></div>
    </div>

    <div class="column">
      <div class="photo">
        <div class="photo-crab" role="img" aria-label="Photo of Singapore chilli crab garnished with herbs"></div>
        <div class="photo-pair">
          <div class="photo-nasi" role="img" aria-label="Photo of nasi lemak with egg and sambal"></div>
          <div class="photo-murtabak" role="img" aria-label="Photo of murtabak drizzled with chili sauce"></div>
        </div>
      </div>
      <h2 class="section-title">Roti</h2>
      <div class="dish"><div class="dish-head"><span class="dish-name">Made famous in Taman Serasi Singapore</span><span class="dish-price">$15</span></div>
        <p class="dish-desc">Baguette loaf grilled with a topping choice of curried chicken / spiced beef or seasonal veggies cooked with egg and drizzled with chili sauce</p></div>
      <div class="dish"><div class="dish-head"><span class="dish-name">Roti Prata (2 pieces)</span><span class="dish-price">$10</span></div>
        <p class="dish-desc">A traditional crispy street food flat bread accompanied with choice of chicken or veg curry for dipping</p></div>
      <div class="dish"><div class="dish-head"><span class="dish-name">Roti Jala - Malay netted crepe</span><span class="dish-price">$15</span></div>
        <p class="dish-desc">Flour &amp; egg based batter spiced with tumeric and cumin accompanied with choice of chicken or veg curry</p></div>
      <div class="dish"><div class="dish-head"><span class="dish-name">Murtabak - stuffed prata</span><span class="dish-price">$15</span></div>
        <p class="dish-desc">Flour based crispy flat bread stuffed with choice of double cooked chicken curry, sauteed beef or seasonal veg curry</p></div>
    </div>
  </div>

  <div class="page">
    <div class="column">
      <h2 class="section-title">Noodles</h2>
      <div class="dish"><div class="dish-head"><span class="dish-name">Wonton Mee</span><span class="dish-price">$15</span></div>
        <p class="dish-desc">Wonton noodles tossed in sweet dark soy sauce, sesame oil topped with pickled chili, cucumber &amp; broth with choice of bbq pork, chicken or prawns and fried crispy wontons</p></div>
      <div class="dish"><div class="dish-head"><span class="dish-name">Seafood mee goreng</span><span class="dish-price">$18</span></div>
        <p class="dish-desc">Wok fried Malay style egg noodles in a homemade chili paste with prawns and squid topped with fried egg</p></div>
      <div class="dish"><div class="dish-head"><span class="dish-name">Veggie mee goreng V</span><span class="dish-price">$15</span></div>
        <p class="dish-desc">Wok fried Malay style egg noodles in homemade chili paste with seasonal veggies &amp; tofu</p></div>
      <div class="dish"><div class="dish-head"><span class="dish-name">Char Kway Teow</span><span class="dish-price">$15</span></div>
        <p class="dish-desc">Wok fried rice cake strips in sweet dark soy sauce, fish oil, chili paste with seafood topped with beansprouts</p></div>
      <div class="dish"><div class="dish-head"><span class="dish-name">Laksa Ala Katong Singapore</span><span class="dish-price">$18</span></div>
        <p class="dish-desc">A Peranakan style prawn based broth noodles with prawns, squid and mussels topped with boiled egg &amp; fried tofu cubes</p></div>
      <div class="dish"><div class="dish-head"><span class="dish-name">Hor Fun Noodles</span><span class="dish-price">$16</span></div>
        <p class="dish-desc">Flat rice noodles stir fried with dark sweet soy sauce and a choice of seafood or pork in a silky egg gravy</p></div>
      <div class="photo photo-gado" role="img" aria-label="Photo of gado gado salad with egg, tofu and crackers"></div>
    </div>

    <div class="column">
      <h2 class="section-title">Rice</h2>
      <div class="dish"><div class="dish-head"><span class="dish-name">Singapore Chicken rice (Family style sharing)</span></div>
        <div class="dish-head"><span class="dish-name">Half chicken for 2 pax</span><span class="dish-price">$20</span></div>
        <div class="dish-head"><span class="dish-name">Whole chicken for 4 pax</span><span class="dish-price">$35</span></div>
        <p class="dish-desc">The Singapore classic - aromatic roasted chicken with fragrant rice cooked in a chicken broth accompanied by seasonal veg in oyster sauce and ginger sweet chili dip</p></div>
      <div class="dish"><div class="dish-head"><span class="dish-name">Nasi Lemak 2 pax</span><span class="dish-price">$18</span></div>
        <p class="dish-desc">Jasmine rice cooked in coconut cream infused in pandan leaves, comes with condiments of fried egg, ikan bilis, toasted nuts, crispy fried chicken and shrimp based sambal</p></div>
      <div class="dish"><div class="dish-head"><span class="dish-name">Fried Rice</span><span class="dish-price">$18</span></div>
        <p class="dish-desc">Chinese style fried rice with choice of chicken, beef or veg in sesame oil &amp; fish sauce</p></div>
      <div class="dish"><div class="dish-head"><span class="dish-name">Black Pepper Rice</span><span class="dish-price">$18</span></div>
        <p class="dish-desc">Fragrant white rice accompanied by a choice of tender beef, chicken or seafood in a black pepper sauce</p></div>

      <h2 class="section-title" style="margin-top:10px">Desserts</h2>
      <div class="dish"><div class="dish-head"><span class="dish-name">Apam Balek</span><span class="dish-price">$10</span></div>
        <p class="dish-desc">Malay style sweet pancake filled with crushed toasted nuts, caramelised onions accompanied with ice cream and caramelised condensed milk</p></div>
      <div class="dish"><div class="dish-head"><span class="dish-name">Kueh Dadar</span><span class="dish-price">$10</span></div>
        <p class="dish-desc">Grated coconut cooked in gula melaka (palm sugar) and wrapped in a pandan infused crepe</p></div>
      <div class="dish"><div class="dish-head"><span class="dish-name">Sago Gula Melaka</span><span class="dish-price">$10</span></div>
        <p class="dish-desc">Creamy tapioca pearl pudding served with thick caramelised palm sugar</p></div>
      <div class="dish"><div class="dish-head"><span class="dish-name">Kueh Seri Muke</span><span class="dish-price">$10</span></div>
        <p class="dish-desc">Steamed layer of Glutinous rice and pandan infused coconut milk topped with toasted desiccated coconut</p></div>
    </div>
  </div>
</main>

</body>
</html>
```